Letterhead and Business card for Construction company

We need a letterhead and business card with our new company logo. We are based in NY. We develop and build properties.

The design should incorporate some unique feature from the logo (shape, font...). it should look like an extension from it.

Design should be clean and elegant, professional, not too busy.

The letterhead should include:
Logo (attached)
Address
Phone
Email

Please find the attached logo images and AI file.

Target Market(s)

Construction industry professionals

Industry/Entity Type

Construction, Development

Font styles to use
Sans Serif

Colors

Designer to choose colors to be used in the design.

Requirements
Must have
• Design should incorporate logo elements, additional assets are welcome. I'd like to see some other shapes / images invorporated too.

```html
<!DOCTYPE html>
<html lang="en">
<head>
<meta charset="utf-8">
<title>Norvane Builders – Business Card</title>
<link rel="stylesheet" href="https://fonts.googleapis.com/css2?family=Karla:wght@400;500;700&display=swap">
<style>
  :root {
    --backdrop: #2b2b2d;
    --card: #262527;
    --ink: #ffffff;
    --ink-soft: #e6e6e6;
    --accent: #f07d1a;
    --art-light: #8a8a8a;
    --art-dark: #1a1a1a;
  }
  * { box-sizing: border-box; margin: 0; padding: 0; }
  html, body { width: 1200px; height: 874px; overflow: hidden; }
  body {
    background: var(--backdrop);
    font-family: "Karla", sans-serif;
    color: var(--ink);
    position: relative;
  }
  .card {
    position: absolute;
    left: 320px;
    width: 560px;
    height: 320px;
    background: var(--card);
    overflow: hidden;
  }
  .card--front { top: 105px; display: flex; align-items: center; justify-content: center; }
  .card--back { top: 449px; }

  .brand {
    display: flex;
    align-items: center;
    gap: 12px;
    font-weight: 700;
    font-size: 34px;
    letter-spacing: 0.04em;
    text-transform: uppercase;
    color: var(--ink);
    white-space: nowrap;
  }
  .brand__mark { width: 22px; height: 22px; background: var(--ink); flex: none; }

  .card--back .brand {
    position: absolute;
    left: 36px;
    top: 40px;
    font-size: 24px;
    gap: 10px;
  }
  .card--back .brand__mark { width: 16px; height: 16px; }

  .person { position: absolute; left: 36px; top: 104px; }
  .person__name {
    font-weight: 700;
    font-size: 21px;
    color: var(--accent);
    text-transform: uppercase;
    letter-spacing: 0.01em;
  }
  .person__title { font-size: 13px; color: var(--ink-soft); margin-top: 2px; }

  .contacts {
    position: absolute;
    left: 36px;
    top: 168px;
    list-style: none;
    font-size: 13px;
    line-height: 1.45;
    color: var(--ink-soft);
  }
  .contacts li { display: flex; align-items: flex-start; gap: 9px; margin-bottom: 3px; }
  .contacts svg { width: 11px; height: 11px; margin-top: 3px; flex: none; fill: var(--accent); }

  .art-area {
    position: absolute;
    right: 40px;
    bottom: 0;
    width: 210px;
    height: 200px;
    background: linear-gradient(90deg, var(--art-light), var(--art-dark));
  }
</style>
</head>
<body>
  <section class="card card--front">
    <div class="brand"><span class="brand__mark"></span>Norvane Builders</div>
  </section>

  <section class="card card--back">
    <div class="brand"><span class="brand__mark"></span>Norvane Builders</div>

    <div class="person">
      <p class="person__name">Daniel Reyes</p>
      <p class="person__title">President</p>
    </div>

    <ul class="contacts">
      <li>
        <svg viewBox="0 0 12 12"><path d="M6 0a4 4 0 0 0-4 4c0 3 4 8 4 8s4-5 4-8a4 4 0 0 0-4-4zm0 5.6A1.6 1.6 0 1 1 6 2.4a1.6 1.6 0 0 1 0 3.2z"/></svg>
        <span>214 Cedar Ridge Road<br>Albany, New York 12207</span>
      </li>
      <li>
        <svg viewBox="0 0 12 12"><path d="M2.5 0.5l2 2-1.2 1.6c.8 1.6 2 2.8 3.6 3.6l1.6-1.2 2 2-1.2 2C4.6 10.6 1.4 7.4.5 2.7z"/></svg>
        <span>518-204-7731</span>
      </li>
      <li>
        <svg viewBox="0 0 12 12"><path d="M0 2h12v1L6 7 0 3zM0 4.4l6 4 6-4V10H0z"/></svg>
        <span>hello@norvanebuilders.com</span>
      </li>
      <li>
        <svg viewBox="0 0 12 12"><circle cx="6" cy="6" r="5.5"/></svg>
        <span>norvanebuilders.com</span>
      </li>
    </ul>

    <div class="art-area" role="img" aria-label="Decorative artwork of building towers in silver to black tones"></div>
  </section>
</body>
</html>
```